2026 Compostable Stand up Pouch Redesign

Project Overview
We are a natural dog bakery focused on simple, healthy ingredients and earth-friendly packaging. As the first step in a rebrand, we are redesigning our 6 oz stand-up pouch using new compostable packaging materials.
New pouch is the same size and structure as current (template provided)
Files included:
Existing Art template (PDF + JPG)
Photos of current packaging (for reference only)
Copy of existing logo (Meadowlark Treat Kitchen)
Copy of future logo (Birchwood Natural Bakery)
This redesign should feel like a clear upgrade—more refined, more intentional, and more aligned with sustainability.
⚠️ IMPORTANT LAYOUT CONSTRAINT (PLEASE READ)
The new pouch has a full-width horizontal window.
Design elements may ONLY appear above and below the window
No design elements can be placed to the left or right of the window
A 4.5" W x 3.5" H blank space above the window must be preserved
This is reserved for applied product labels
Keep this area completely clean (no textures, patterns, or graphics)
Submissions that ignore these elements will not be considered.
Brand Direction & Style
We are looking for a design that feels:
Natural and ingredient-focused
Eco-conscious and sustainable
Clean and elevated (not rustic, not overly playful)
Warm and trustworthy
Avoid:
Neon or bright artificial colors
Loud, busy, or overly commercial designs
Cartoon-heavy or overly whimsical styles
Color Direction
Our current packaging is kraft brown, but the new material allows full-color printing. We are looking for:
Nature-inspired colors only
Greens, muted blues, warm browns, soft earth tones
Background color is flexible within this palette
Must work with:
Current logo: Meadowlark Treat Kitchen
Future logo: Birchwood Natural Bakery
👉 For this project, use Meadowlark Treat Kitchen logo only
Front of Pouch Requirements
Do NOT include logo on pouch front
(Logo will be on applied labels)
Required Elements
Tagline: Simple, Healthy Ingredients. Earth Friendly Packaging.
Compostable Messaging (REQUIRED):
Must clearly communicate that packaging is compostable
Optional placement:
Tear-off strip near hang hole
BUT must also appear somewhere on the main pouch design
Origin Callout:
“Hand Made in the Pacific Northwest”
Can be a badge, stamp, or graphic (open to redesign)
Icons (Highly Encouraged)
We would like to explore a clean, minimal icon set for:
No Corn
No Wheat
No Soy
No GMOs
Compostable Packaging
(Keep icons simple, clean, and consistent with natural aesthetic)
Back of Pouch Requirements
Messaging Direction
Do NOT use: “The healthiest pet bakery in the US”
Instead, build around:
Simple, Healthy Ingredients. Earth Friendly Packaging.
Content
“Our Recipes” bullet points (from current packaging – still valid)
Sustainability messaging:
Include reference to reducing our “carbon pawprint”
Emphasize eco-friendly materials and practices
Design Direction
Open to new layout and graphics
Should visually reinforce:
Clean ingredients
Natural sourcing
Sustainability
Printing Considerations
Design should be mindful of production scalability:
Should translate well to both digital and roto printing
Avoid overly complex gradients or excessive color layering
Creative Freedom (Important)
While we have outlined structure and constraints, we are intentionally leaving visual interpretation open.
We welcome:
Fresh layout ideas
Refined graphic elements
Elevated visual storytelling
We are especially interested in designs that feel:
Thoughtful
Clean
Naturally premium
Any design submission that includes loud, neon, or "aggressive" color schemes or a mass market appeal will be eliminated immediately. We are a premium, natural dog bakery found in independent stores only.
UPDATED & IMPORTANT DESIGN REQUIREMENTS (PLEASE READ)
This pouch is a base design used across all flavors. A separate product label will be applied.
A clearly defined blank area must be left for label placement (do not incorporate into artwork).
The product viewing window is fixed:
Size and placement must match the template exactly
Do not resize, reposition, or redesign the window
Designs that do not follow these requirements will not be considered.
Please review the discussion board for additional feedback and direction before submitting revisions.

```html
<!DOCTYPE html>
<html lang="en">
<head>
<meta charset="utf-8">
<title>Meadowlark Treat Kitchen – Compostable Pouch</title>
<link rel="stylesheet" href="https://fonts.googleapis.com/css2?family=Lato:wght@400;700;900&family=Playfair+Display:wght@500;600;700&display=swap">
<style>
  :root{
    --bg:#e6e6e3;
    --cream:#ede3d0;
    --cream-shade:#e3d7c1;
    --green-dark:#1f4a2c;
    --green-band:#2f5e3c;
    --green-text:#1e4a2d;
    --brown:#6b4531;
    --brown-soft:#a0764f;
    --label:#f7f7f5;
    --treat-a:#c9ad85;
    --treat-b:#9d7f5a;
    --ink-light:#f2ede2;
  }
  *{box-sizing:border-box;margin:0;padding:0}
  html,body{width:1200px;height:1104px;overflow:hidden;background:var(--bg)}
  .canvas{position:relative;width:1200px;height:1104px}
  .pouch{position:absolute;top:188px;width:500px;height:767px;background:var(--cream);overflow:hidden}
  .pouch--front{left:88px}
  .pouch--back{left:612px}

  /* front */
  .compost-tab{position:absolute;left:141px;top:0;width:215px;height:42px;background:var(--green-dark);border-radius:0 0 10px 10px;color:var(--ink-light);font:700 15px/42px "Lato",sans-serif;text-align:center}
  .tear-strip{position:absolute;left:8px;right:8px;top:64px;display:flex;align-items:center;gap:8px;color:var(--brown);font:900 10px "Lato",sans-serif;letter-spacing:2.4px;white-space:nowrap}
  .tear-strip::before,.tear-strip::after{content:"";flex:1;border-top:1.5px dotted var(--brown-soft)}
  .zip-line{position:absolute;left:20px;right:20px;top:103px;height:6px;background:var(--cream-shade);border-radius:3px}
  .tagline{position:absolute;left:0;right:0;top:134px;text-align:center;color:var(--green-text);font:700 32px/40px "Playfair Display",serif}
  .label-area{position:absolute;left:64px;top:236px;width:369px;height:300px;background:var(--label);border-radius:12px}
  .window{position:absolute;left:26px;right:26px;top:540px;height:99px;background:linear-gradient(180deg,var(--treat-a),var(--treat-b))}
  .band{position:absolute;left:0;right:0;bottom:0;background:var(--green-band)}
  .pouch--front .band{top:639px}
  .icon-row{position:absolute;left:44px;top:25px;display:flex;gap:10px}
  .icon{width:40px;text-align:center;color:var(--ink-light);font:400 7.5px/9px "Lato",sans-serif}
  .icon svg{display:block;margin:0 auto 5px;width:36px;height:36px}
  .origin{position:absolute;left:316px;top:16px;width:90px;text-align:center;color:var(--brown-soft);font:700 11.5px/14px "Lato",sans-serif}
  .origin svg{display:block;margin:0 auto 6px}

  /* back */
  .brand-mark{position:absolute;left:0;right:0;top:100px;text-align:center}
  .brand-mark .dot{width:60px;height:60px;border:2px solid var(--green-dark);border-radius:50%;margin:0 auto 12px}
  .brand-name{color:var(--green-dark);font:700 30px/34px "Playfair Display",serif}
  .recipes-badge{position:absolute;left:137px;top:302px;width:212px;height:46px;background:var(--green-dark);border-radius:5px;color:var(--ink-light);font:600 27px/46px "Playfair Display",serif;text-align:center}
  .recipe{position:absolute;display:flex;align-items:flex-start;gap:9px;color:var(--green-text);font:400 15.5px/20px "Lato",sans-serif}
  .recipe svg{flex:none}
  .r1{left:63px;top:363px;align-items:center}
  .r2{left:247px;top:363px;align-items:center}
  .r3{left:60px;top:411px}
  .r4{left:247px;top:411px}
  .divider{position:absolute;left:74px;width:336px;top:481px;border-top:1.5px dotted var(--green-band)}
  .pawprint{position:absolute;left:0;right:0;top:490px;text-align:center;color:var(--green-text)}
  .pawprint h2{font:600 21px/28px "Playfair Display",serif;margin-bottom:8px}
  .pawprint p{font:400 11px/14.5px "Lato",sans-serif;margin-bottom:8px}
  .pouch--back .band{top:633px}
  .material-pill{position:absolute;left:142px;top:605px;width:198px;height:42px;background:var(--brown);border-radius:21px;display:flex;align-items:center;gap:8px;padding-left:16px;color:var(--ink-light);font:600 11px/13px "Playfair Display",serif;z-index:2}
  .contact{position:absolute;left:0;right:0;top:27px;text-align:center;color:var(--ink-light)}
  .contact .friends{font:700 11.5px "Playfair Display",serif;letter-spacing:.4px;margin-bottom:8px}
  .contact p{font:400 10.5px/14px "Lato",sans-serif}
</style>
</head>
<body>
<main class="canvas">

  <section class="pouch pouch--front" aria-label="Pouch front">
    <div class="compost-tab">100% home compostable</div>
    <div class="tear-strip">TEAR-OFF STRIP NEAR HANG HOLE</div>
    <div class="zip-line"></div>
    <h1 class="tagline">Simple, Healthy Ingredients.<br>Earth Friendly Packaging.</h1>
    <div class="label-area" aria-label="Blank area for applied product label"></div>
    <div class="window" role="img" aria-label="Clear window showing bone-shaped dog biscuits"></div>
    <div class="band">
      <div class="icon-row">
        <div class="icon">
          <svg viewBox="0 0 36 36" fill="none" stroke="currentColor" stroke-width="1.3"><circle cx="18" cy="18" r="16"/><ellipse cx="18" cy="17" rx="4.5" ry="8"/><path d="M18 25v6M13 29c2-2 3-4 5-4s3 2 5 4"/><path d="M7 29L29 7"/></svg>
          NO CORN
        </div>
        <div class="icon">
          <svg viewBox="0 0 36 36" fill="none" stroke="currentColor" stroke-width="1.3"><circle cx="18" cy="18" r="16"/><path d="M18 8v22"/><path d="M18 12c-3 0-4-2-4-4M18 12c3 0 4-2 4-4M18 18c-3 0-4-2-4-4M18 18c3 0 4-2 4-4M18 24c-3 0-4-2-4-4M18 24c3 0 4-2 4-4"/><path d="M7 29L29 7"/></svg>
          NO WHEAT
        </div>
        <div class="icon">
          <svg viewBox="0 0 36 36" fill="none" stroke="currentColor" stroke-width="1.3"><circle cx="18" cy="18" r="16"/><rect x="9" y="14" width="18" height="8" rx="4" transform="rotate(-40 18 18)"/><circle cx="14.5" cy="21" r="1.6"/><circle cx="21.5" cy="15" r="1.6"/><path d="M7 7l22 22"/></svg>
          NO SOY
        </div>
        <div class="icon">
          <svg viewBox="0 0 36 36" fill="none" stroke="currentColor" stroke-width="1.3"><circle cx="18" cy="18" r="16"/><path d="M13 8c0 7 10 13 10 20M23 8c0 7-10 13-10 20M14 12h8M14 24h8M16 18h4"/><path d="M7 29L29 7"/></svg>
          NO GMO
        </div>
        <div class="icon">
          <svg viewBox="0 0 36 36" fill="none" stroke="currentColor" stroke-width="1.3"><circle cx="18" cy="18" r="16"/><path d="M11 14a8 8 0 0 1 12-4l2-2v6h-6l2-2a5 5 0 0 0-7 3"/><path d="M25 22a8 8 0 0 1-12 4l-2 2v-6h6l-2 2a5 5 0 0 0 7-3"/></svg>
          COMPOSTABLE PACKAGING
        </div>
      </div>
      <div class="origin">
        <svg width="22" height="30" viewBox="0 0 22 30" fill="none" stroke="currentColor" stroke-width="1.3"><path d="M11 1L4 10h4L2 18h5L1 25h20l-6-7h5l-6-8h4z"/><path d="M11 25v4"/></svg>
        Hand Made<br>In The Pacific<br>Northwest
      </div>
    </div>
  </section>

  <section class="pouch pouch--back" aria-label="Pouch back">
    <div class="zip-line"></div>
    <div class="brand-mark">
      <div class="dot"></div>
      <div class="brand-name">Meadowlark<br>Treat Kitchen</div>
    </div>
    <h2 class="recipes-badge">OUR RECIPES</h2>

    <div class="recipe r1">
      <svg width="30" height="30" viewBox="0 0 30 30" fill="none" stroke="var(--green-dark)" stroke-width="2"><circle cx="15" cy="15" r="13"/><path d="M8 15l5 5 10-12" stroke-width="3"/></svg>
      Clean &amp; Simple
    </div>
    <div class="recipe r2">
      <svg width="32" height="30" viewBox="0 0 32 30" fill="none" stroke="var(--green-dark)" stroke-width="2"><circle cx="16" cy="15" r="13"/><path d="M12 6h8M13 6v8l-6 10h18l-6-10V6"/><path d="M6 26L26 4"/></svg>
      Nothing Artificial
    </div>
    <div class="recipe r3">
      <svg width="40" height="34" viewBox="0 0 40 34" fill="none" stroke="var(--green-dark)" stroke-width="1.6"><path d="M5 18h28c0 8-6 12-14 12S5 26 5 18z" fill="#8fae5a"/><path d="M24 16l6-12"/></svg>
      <span>Handcrafted in<br>Small Batches</span>
    </div>
    <div class="recipe r4">
      <svg width="36" height="34" viewBox="0 0 36 34" fill="none" stroke="var(--green-dark)" stroke-width="1.6"><path d="M4 30C4 16 12 6 22 4c0 14-8 24-18 26z" fill="#8fae5a"/><path d="M4 30L18 12"/></svg>
      <span>Premium Ingredients<br>from the Pacific<br>Northwest</span>
    </div>

    <div class="divider"></div>
    <div class="pawprint">
      <h2>Reducing Our Carbon Pawprint</h2>
      <p>Our focus is on reducing our environmental impact<br>through responsible sourcing and packaging.</p>
      <p>This pouch is made from compostable materials designed<br>to return safely to the earth.</p>
    </div>

    <div class="material-pill">
      <svg width="26" height="26" viewBox="0 0 26 26" fill="none" stroke="currentColor" stroke-width="1.3"><path d="M4 22C4 12 11 5 22 3c0 11-7 18-18 19z"/><path d="M4 22L16 10"/></svg>
      <span>Made with 100% Home<br>Compostable Materials</span>
    </div>

    <div class="band">
      <div class="contact">
        <div class="friends">YOUR FRIENDS @ MEADOWLARK TREAT KITCHEN</div>
        <p>Fernhollow, WA, | 866-555-0148</p>
        <p>www.meadowlarktreatkitchen.com</p>
      </div>
    </div>
  </section>

</main>
</body>
</html>
```